Illustrate 5 network connection diagrams.

I require five network block diagrams to be created to show the connection of equipment and services for non-technical users.
See attached examples for an idea of the design style.

NOTES
-Must be easy to read and understand for non-technical users
-Text must be minimal
-Must use stylised icons and not images of actual equipment
-Colour coding of equipment can be used
-Must be vector images created in Adobe Illustrator
-Images will be for the web and print
-Font: Gotham Book & Gotham Bold
-Size: 1000px (w) x 600px (h)

DIAGRAMS
1. Single laptop for control and output
A laptop connected to a second screen.
The laptop screen is running control software and the second screen is running the output display.

2. Individual laptop for control and output
A laptop running control software.
A second laptop connected to a screen running the output display.

3. Multiple output laptops and screens
Multiple laptops connected to screens individually running the output displays.

4. Chroma key over camera
A second laptop connected to a vision switcher.
A screen connected to the vision switcher.
A camera connected to the vision switcher.
The vision switcher combines the images from the second laptop and the camera onto the screen.

5. Mobile for control and acquisition
A tabled also running the control software.
A smartphone collecting image content to be controlled/outputted.

Mock ups of each diagram are attached

May the best designer conquer!
Thank you

```html
<!DOCTYPE html>
<html lang="en">
<head>
<meta charset="utf-8">
<title>Network Diagram – Chroma Key Over Camera</title>
<link rel="stylesheet" href="https://fonts.googleapis.com/css2?family=Montserrat:wght@400;700&display=swap">
<style>
  :root {
    --bg: #ffffff;
    --link-blue: #1b6db3;
    --device-blue: #1d62a6;
    --link-red: #d2232a;
    --device-red: #c8262c;
    --screen-light: #f7f8f9;
    --screen-mid: #dde1e5;
    --base-light: #f2f3f4;
    --base-dark: #a9adb2;
    --arrow-grey: #9fa3a7;
    --badge-fill: #ffffff;
    --badge-ink: #1a1a1a;
    --cloud-light: #f4f8fb;
    --cloud-dark: #b9cfe2;
    --signal-orange: #f07c1e;
  }
  html, body {
    margin: 0;
    padding: 0;
    overflow: hidden;
    background: var(--bg);
  }
  .canvas {
    width: 1200px;
    height: 720px;
    position: relative;
    overflow: hidden;
    background: var(--bg);
  }
  .diagram { display: block; }
  .link-blue { stroke: var(--link-blue); stroke-width: 6; fill: none; }
  .link-red { stroke: var(--link-red); stroke-width: 6; fill: none; }
  .frame-blue { fill: var(--device-blue); }
  .frame-red { fill: var(--device-red); }
  .screen { fill: url(#screenGlow); }
  .base { fill: url(#baseShade); }
  .arrow { fill: var(--arrow-grey); }
  .badge { fill: var(--badge-fill); stroke: var(--badge-ink); stroke-width: 2; }
  .badge-label {
    font-family: "Montserrat", sans-serif;
    font-weight: 700;
    font-size: 18px;
    fill: var(--badge-ink);
  }
  .cloud { fill: url(#cloudShade); stroke: var(--cloud-dark); stroke-width: 2; }
  .mast { stroke: #6f8193; stroke-width: 3; fill: none; }
  .signal { stroke: var(--signal-orange); stroke-width: 5; stroke-linecap: round; }
</style>
</head>
<body>
<main class="canvas">
  <svg class="diagram" width="1200" height="720" viewBox="0 0 1200 720" aria-label="Network diagram: two laptops linked through the internet, the receiving laptop feeds a vision switcher with a camera, which outputs to a screen">
    <defs>
      <linearGradient id="screenGlow" x1="0" y1="0" x2="1" y2="1">
        <stop offset="0" stop-color="#ffffff"/>
        <stop offset="0.55" stop-color="#e9ecef"/>
        <stop offset="1" stop-color="#d5dadf"/>
      </linearGradient>
      <linearGradient id="baseShade" x1="0" y1="0" x2="0" y2="1">
        <stop offset="0" stop-color="#f6f7f8"/>
        <stop offset="0.6" stop-color="#d9dcdf"/>
        <stop offset="1" stop-color="#9ea3a8"/>
      </linearGradient>
      <linearGradient id="cloudShade" x1="0" y1="0" x2="0" y2="1">
        <stop offset="0" stop-color="#ffffff"/>
        <stop offset="1" stop-color="#cfdeeb"/>
      </linearGradient>
    </defs>

    <!-- connections -->
    <path class="link-blue" d="M520 129 H367 V210"/>
    <path class="link-blue" d="M608 129 H760 V210"/>
    <line class="link-red" x1="760" y1="291" x2="760" y2="380"/>
    <line class="link-red" x1="813" y1="413" x2="944" y2="413"/>
    <line class="link-red" x1="760" y1="465" x2="760" y2="530"/>

    <!-- internet hub -->
    <g class="hub">
      <line class="signal" x1="564" y1="38" x2="564" y2="48"/>
      <line class="signal" x1="546" y1="44" x2="551" y2="52"/>
      <line class="signal" x1="582" y1="44" x2="577" y2="52"/>
      <line class="signal" x1="534" y1="57" x2="542" y2="61"/>
      <line class="signal" x1="594" y1="57" x2="586" y2="61"/>
      <path class="mast" d="M548 112 L564 64 L580 112 M553 98 H575 M558 82 H570"/>
      <circle cx="564" cy="64" r="5" fill="#8b9aa9"/>
      <path class="cloud" d="M526 150 C508 150 506 126 524 124 C522 108 542 100 552 112 C556 96 582 96 586 112 C600 104 616 116 606 130 C622 134 618 152 602 150 Z"/>
    </g>

    <!-- laptop 1 : sender -->
    <g class="device laptop-send">
      <rect class="frame-blue" x="316" y="207" width="102" height="69" rx="3"/>
      <rect class="screen" x="323" y="214" width="88" height="55"/>
      <path class="arrow" d="M367 222 L396 248 H384 V262 H350 V248 H338 Z"/>
      <path class="base" d="M289 276 H446 L450 284 Q450 291 440 291 H295 Q285 291 285 284 Z"/>
      <circle class="badge" cx="367" cy="207" r="14"/>
      <text class="badge-label" x="367" y="213.5" text-anchor="middle">1</text>
    </g>

    <!-- laptop 2 : receiver -->
    <g class="device laptop-receive">
      <rect class="frame-blue" x="709" y="207" width="102" height="69" rx="3"/>
      <rect class="screen" x="716" y="214" width="88" height="55"/>
      <path class="arrow" d="M743 222 H777 V236 H789 L760 262 L731 236 H743 Z"/>
      <path class="base" d="M681 276 H839 L843 284 Q843 291 833 291 H687 Q677 291 677 284 Z"/>
      <circle class="badge" cx="760" cy="207" r="14"/>
      <text class="badge-label" x="760" y="213.5" text-anchor="middle">2</text>
    </g>

    <!-- vision switcher -->
    <g class="device switcher">
      <rect class="frame-red" x="709" y="377" width="104" height="75" rx="3"/>
      <rect class="screen" x="716" y="384" width="90" height="61"/>
      <path class="base" d="M681 453 H841 L845 459 Q845 465 835 465 H687 Q677 465 677 459 Z"/>
      <circle class="badge" cx="760" cy="377" r="14"/>
      <path d="M750 377 Q760 368 770 377 Q760 386 750 377 Z" fill="#ffffff" stroke="#1a1a1a" stroke-width="1.5"/>
      <circle cx="760" cy="377" r="3.6" fill="#1a1a1a"/>
    </g>

    <!-- camera -->
    <g class="device camera">
      <rect class="frame-red" x="940" y="392" width="62" height="44" rx="6"/>
      <rect x="950" y="386" width="16" height="8" rx="2" fill="var(--device-red)"/>
      <rect x="946" y="398" width="50" height="32" rx="3" fill="#ffffff"/>
      <circle cx="971" cy="414" r="12" fill="var(--device-red)"/>
      <circle cx="971" cy="414" r="7" fill="#e8474d"/>
    </g>

    <!-- output screen -->
    <g class="device laptop-output">
      <rect class="frame-blue" x="683" y="527" width="157" height="96" rx="4"/>
      <rect class="screen" x="692" y="536" width="139" height="78"/>
      <path class="base" d="M645 625 H882 L887 637 Q887 653 872 653 H655 Q640 653 640 637 Z"/>
      <circle class="badge" cx="760" cy="527" r="14"/>
      <text class="badge-label" x="760" y="533.5" text-anchor="middle">2</text>
    </g>
  </svg>
</main>
</body>
</html>
```